Bramblewick Co Leaflet. A5 2-sided Flyer for a UK Lawn Treatment Company

I need an A5 two-side leaflet / flyer designed for my Lawn Treatment company. The leaflet will be for door-drops so quick impact needed. Full colour, both sides. I provide lawn treatments to customers in the Exeter area of Devon. I would like to design to be clear, fresh and reflect the joy a good lawn and garden can bring.

Target Market(s)

Home Owners. 30-80 Years. Familys

Font styles to use
Sans Serif

Colors
9bcb3c
f78f20
ec1f27
33a6d7

Requirements
Must have
• Good front page picture
• Logo
• Contact details on front.
• Call to Action
• More details in Text file included in design.
Nice to have
• Clipart of a family / lady enjoying a lawn.

```html
<!DOCTYPE html>
<html lang="en">
<head>
<meta charset="utf-8">
<title>Bramblewick Co Leaflet</title>
<link href="https://fonts.googleapis.com/css2?family=Comfortaa:wght@300&family=Roboto+Condensed:ital,wght@0,400;0,700;1,400;1,700&family=Roboto+Slab:wght@300;400&family=Exo+2:ital,wght@0,700;1,700&family=Fredoka:wght@600&display=swap" rel="stylesheet">
<style>
:root{
  --page:#d9dadc;
  --lime:#9bcb3c;
  --lime-bright:#d8ec1c;
  --grass:#5aa51c;
  --grass-dark:#2f6a12;
  --yellow:#fff21a;
  --orange:#f78f20;
  --red:#ec1f27;
  --blue:#33a6d7;
  --teal-head:#0f5d66;
  --ink:#1c1c1c;
  --tag:#2e5a2a;
  --purple:#7b4ba3;
  --plum:#8e3f8f;
  --brown:#8a4b3b;
  --pink:#e52a8c;
  --aqua:#45bccb;
  --logo-green:#3a9a2e;
}
*{box-sizing:border-box;margin:0;padding:0}
html,body{width:1200px;height:1200px;overflow:hidden;background:var(--page);font-family:"Roboto Condensed",sans-serif}
.flyer{position:absolute;width:770px;height:537px;overflow:hidden;box-shadow:6px 8px 14px rgba(0,0,0,.35)}
.flyer-front{left:50px;top:32px}
.flyer-back{left:309px;top:602px}

/* front */
.front-photo{position:absolute;inset:0;background:
  radial-gradient(ellipse at 15% 0%,#f4f640 0%,transparent 55%),
  linear-gradient(160deg,#e6f21e 0%,#b9df1f 45%,#6fb81c 100%)}
.front-photo .figure{position:absolute;right:0;top:120px;width:300px;height:417px;background:linear-gradient(120deg,rgba(255,255,255,0) 0%,rgba(245,230,215,.55) 45%,rgba(215,180,140,.55) 100%)}
.orbit{position:absolute;inset:0}
.logo{position:absolute;display:flex;align-items:center;gap:8px;font-family:"Roboto Condensed",sans-serif;font-weight:700;color:var(--logo-green);white-space:nowrap}
.logo .mark{width:18px;height:18px;border-radius:50%;background:var(--logo-green)}
.front-logo{left:540px;top:110px;font-size:28px}
.stars{position:absolute;font-size:10px;letter-spacing:3px;color:var(--purple)}
.bubble{position:absolute;padding:9px 10px;border-radius:8px;font-size:10px;line-height:1.3;font-style:italic;color:#fff;box-shadow:3px 4px 0 rgba(0,0,0,.18)}
.bubble::after{content:"";position:absolute;bottom:-9px;right:28px;border-left:6px solid transparent;border-right:6px solid transparent;border-top:10px solid var(--c)}
.bubble{background:var(--c)}
.who{position:absolute;font-size:12px;font-weight:700;font-style:italic;color:var(--ink)}
.heading-testimonials{position:absolute;left:176px;top:222px;font-family:"Fredoka",sans-serif;font-size:26px;font-weight:600;color:var(--teal-head);letter-spacing:1px}
.contact{position:absolute;left:30px;color:var(--ink)}
.contact .label{font-size:12px;font-style:italic;font-weight:700}
.contact .number{font-family:"Exo 2",sans-serif;font-size:23px;font-weight:700;line-height:1.1}
.web-pill{position:absolute;left:0;top:460px;width:184px;height:46px;border-radius:0 10px 10px 0;background:linear-gradient(90deg,var(--orange),var(--red));color:#fff;padding:6px 0 0 28px}
.web-pill .small{font-size:10px;font-style:italic;font-weight:700}
.web-pill .url{font-size:16px;font-style:italic;font-weight:700}

/* back */
.grass-panel{position:absolute;left:0;top:0;width:261px;height:537px;background:linear-gradient(180deg,#4f9a1f 0%,#6cb32b 40%,#3f8a18 100%)}
.panel-title{position:absolute;left:35px;top:40px;width:220px;font-family:"Comfortaa",sans-serif;font-weight:300;font-size:27px;line-height:1;color:#fff}
.panel-points{position:absolute;left:35px;top:180px;width:220px;font-family:"Roboto Slab",serif;font-weight:300;font-size:17px;line-height:1.1;color:var(--yellow)}
.panel-points p{margin-bottom:18px}
.compare{position:absolute;left:15px;top:358px;width:228px;height:98px;padding:10px;border-radius:8px;background:rgba(255,255,255,.35);display:flex;gap:2px}
.compare .shot{flex:1;position:relative}
.compare .before{background:linear-gradient(180deg,#587a3c 0%,#9a9a52 60%,#b09a56 100%)}
.compare .after{background:linear-gradient(180deg,#4f7a3a 0%,#5ea22e 55%,#4fa028 100%)}
.compare span{position:absolute;left:8px;bottom:4px;font-size:10px;font-style:italic;color:#fff}
.panel-band{position:absolute;left:0;top:485px;width:261px;height:52px;background:rgba(40,70,20,.75);padding:8px 0 0 20px;font-size:13px;font-weight:700;font-style:italic;line-height:1.05;color:var(--yellow)}
.info{position:absolute;left:261px;top:0;width:509px;height:537px;background:var(--yellow)}
.info-photo{position:absolute;left:0;top:334px;width:509px;height:203px;background:linear-gradient(180deg,var(--yellow) 0%,#cde61e 25%,#8ec826 70%,#6bb51f 100%)}
.back-logo{left:300px;top:30px;font-size:26px}
.tag{position:absolute;left:46px;height:19px;padding:0 22px 0 10px;background:var(--tag);color:#fff;font-family:"Roboto Slab",serif;font-size:13px;line-height:19px;clip-path:polygon(0 0,100% 0,calc(100% - 12px) 100%,0 100%)}
.copy{position:absolute;left:52px;width:430px;font-size:11.5px;line-height:1.1;color:var(--ink);letter-spacing:-.2px}
.treatments{position:absolute;left:46px;top:333px;display:flex;gap:18px;font-size:12px;font-weight:700;color:var(--ink)}
.treatments ul{list-style:none}
.treatments li{margin-bottom:3px;padding-left:12px;position:relative}
.treatments li::before{content:"";position:absolute;left:0;top:5px;width:5px;height:5px;border-radius:50%;background:var(--red)}
.call-strip{position:absolute;left:0;top:485px;width:509px;height:52px;background:rgba(255,255,255,.12)}
.call{position:absolute;right:22px;top:498px;display:flex;align-items:center;gap:4px;color:var(--tag)}
.call small{font-size:10px;font-weight:700;line-height:.8;width:22px}
.call b{font-family:"Exo 2",sans-serif;font-size:25px}
</style>
</head>
<body>

<section class="flyer flyer-front">
  <div class="front-photo" role="img" aria-label="Photo of a sunlit lawn with a woman sitting on the grass looking at her phone"><div class="figure"></div></div>

  <svg class="orbit" width="770" height="537" viewBox="0 0 770 537" aria-hidden="true">
    <ellipse cx="330" cy="235" rx="300" ry="200" fill="none" stroke="#2a3a20" stroke-width="1.3" stroke-dasharray="2 4"/>
    <ellipse cx="300" cy="250" rx="230" ry="180" fill="none" stroke="#2a3a20" stroke-width="1.2" stroke-dasharray="2 4"/>
    <circle cx="636" cy="266" r="3" fill="#2a3a20"/><circle cx="577" cy="355" r="3" fill="#2a3a20"/><circle cx="625" cy="205" r="3" fill="#2a3a20"/>
  </svg>

  <div class="logo front-logo"><span class="mark"></span>Bramblewick Co</div>

  <div class="stars" style="left:78px;top:24px">★★★★★</div>
  <div class="bubble" style="--c:var(--purple);left:58px;top:40px;width:134px;transform:rotate(7deg)">Thank you for keeping our lawn in great shape for so long, I've been really pleased with how it has looked since you took care of it.</div>
  <div class="who" style="left:158px;top:132px">Alan</div>

  <div class="stars" style="left:218px;top:60px;color:var(--blue)">★★★★★</div>
  <div class="bubble" style="--c:var(--aqua);left:208px;top:76px;width:134px;color:#1d3f7a">We are so grateful for your skill over the years. We've seen our lawn thrive and you changed a neglected difficult garden to one that everyone comments on.</div>
  <div class="who" style="left:294px;top:180px">Morwen</div>

  <div class="stars" style="left:374px;top:22px">★★★★★</div>
  <div class="bubble" style="--c:var(--plum);left:374px;top:44px;width:134px;transform:rotate(-5deg)">Thank you for the lawn service you have provided over the years. It is reassuring to have you come round as I know you carried out the service as promised unlike other lawn service companies I have dealt with.</div>
  <div class="who" style="left:478px;top:168px">Gareth</div>

  <div class="stars" style="left:38px;top:146px;color:var(--brown)">★★★★</div>
  <div class="bubble" style="--c:var(--brown);left:38px;top:164px;width:138px;transform:rotate(-10deg)">My lawn has never looked better since the day that you started to look after it for me.</div>
  <div class="who" style="left:128px;top:212px">Mr. Pell</div>

  <div class="heading-testimonials">TESTIMONIALS</div>

  <div class="stars" style="left:86px;top:230px;color:var(--orange)">★★★★★</div>
  <div class="bubble" style="--c:var(--orange);left:70px;top:246px;width:132px;transform:rotate(6deg)">We have very much appreciated your service over the last four years, and especially value your reliability and perennial cheerfulness!</div>
  <div class="who" style="left:142px;top:342px">Ronald</div>

  <div class="stars" style="left:228px;top:254px;color:var(--red)">★★★★★</div>
  <div class="bubble" style="--c:var(--red);left:222px;top:272px;width:134px;transform:rotate(-5deg)">It has been a pleasure to do business with you over the last few years and the lawn you leave us with is infinitely healthier and more attractive than the lawn you inherited!</div>
  <div class="who" style="left:310px;top:372px">Maureen</div>

  <div class="stars" style="left:388px;top:190px;color:var(--pink)">★★★★★</div>
  <div class="bubble" style="--c:var(--pink);left:378px;top:206px;width:132px;transform:rotate(3deg)">Your company have been fantastic. Reliable, good advice, effective treatments and you are very knowledgeable about lawns. You really do know what you are talking about! Cannot recommend you highly enough.</div>
  <div class="who" style="left:462px;top:352px">Gareth</div>

  <div class="contact" style="top:368px"><div class="label">Call today on</div><div class="number">01632 960418</div></div>
  <div class="contact" style="top:412px"><div class="label">or text</div><div class="number">07700 900512</div></div>

  <div class="web-pill"><div class="small">to book your lawn survey</div><div class="url">bramblewickco.uk</div></div>
</section>

<section class="flyer flyer-back">
  <div class="grass-panel" role="img" aria-label="Close-up photo of tall green grass"></div>
  <h1 class="panel-title">Treatments &amp; advice to keep your lawn looking nice.</h1>
  <div class="panel-points">
    <p>Brand new to the area!</p>
    <p>8 Years experience maintaining the finest lawns of Cheshire</p>
    <p>Complete Satisfaction Guarantee</p>
  </div>
  <div class="compare">
    <div class="shot before" role="img" aria-label="Before photo of a patchy brown lawn"><span>Before</span></div>
    <div class="shot after" role="img" aria-label="After photo of a lush green lawn"><span>After</span></div>
  </div>
  <div class="panel-band">Save time and money and leave<br>your lawn to an expert.</div>

  <div class="info">
    <div class="info-photo" role="img" aria-label="Photo of a woman lying on a green lawn reading"></div>
    <div class="logo back-logo"><span class="mark"></span>Bramblewick Co</div>

    <div class="tag" style="top:62px">For a beautiful weed-free lawn</div>
    <p class="copy" style="top:88px">Call Bramblewick Co today and start your journey to a wonderful, lush, green lawn you and your family can enjoy. Arrange a no-obligation lawn survey and quotation at a time to suit you. Call 01632 960418 now.</p>

    <div class="tag" style="top:132px">I will understand your lawn</div>
    <p class="copy" style="top:158px">Every lawn is unique. I take time to gain a comprehensive understanding of your lawn and its situation. I will also listen to you and understand your problems and your aspirations for your grass.</p>

    <div class="tag" style="top:202px">Your lawn treatments</div>
    <p class="copy" style="top:229px">I will creat a custom treatment programme tailored to your lawn. I may also recommend some remedial treatments to correct any existing problems. There is no contract to sign. I guarantee all treatments.</p>

    <div class="tag" style="top:271px">Industry-leading lawn care</div>
    <p class="copy" style="top:298px">I have 8 years of experience in the leading edge of domestic lawn care. I have a comprehensive range of treatments including:</p>

    <div class="treatments">
      <ul><li>Scarification</li><li>Aeration</li><li>Moss Control</li><li>Overseeding</li><li>Top Dressing</li><li>Lawn Repairs</li></ul>
      <ul><li>Fertilisation &amp; Weed Control</li><li>Pest &amp; Disease Management</li><li>Special Event Preparation</li></ul>
    </div>

    <div class="call-strip"></div>
    <div class="call"><small>Call Today</small><b>01632 960418</b></div>
  </div>
</section>

</body>
</html>
```